Old Scholl Hip Hop Party Design

I need a flyer which shows some old stuff from the 80s, 90s, Hip Hop and RnB
the party is called "Midnight Velvet Parade" its every week on a tuesday
We are a club so the style should be modern and stylisch, i put some samples from old flyers and our logo attached

Target Market(s)

Bar / Club Party Scene

Industry/Entity Type

School

```html
<!DOCTYPE html>
<html lang="en">
<head>
<meta charset="utf-8">
<title>Midnight Velvet Parade – Flyer</title>
<link href="https://fonts.googleapis.com/css2?family=Oswald:wght@300;400;500;700&display=swap" rel="stylesheet">
<style>
  :root {
    --backdrop: #e4e4e4;
    --paper-light: #f8eaa6;
    --paper-mid: #f1d35a;
    --paper-deep: #d9a92b;
    --torn-grey: #d6d6d6;
    --torn-edge: #9c9c9c;
    --ink: #141414;
    --box-tone-a: #cfc5a0;
    --box-tone-b: #8d7a3c;
  }
  * { margin: 0; padding: 0; box-sizing: border-box; }
  html, body {
    width: 1200px;
    height: 900px;
    overflow: hidden;
    background: var(--backdrop);
  }
  .canvas {
    position: relative;
    width: 1200px;
    height: 900px;
  }
  .flyer {
    position: absolute;
    left: 285px;
    top: 12px;
    width: 630px;
    height: 876px;
    overflow: hidden;
    background:
      radial-gradient(ellipse 70% 55% at 40% 78%, var(--paper-light) 0%, rgba(248,234,166,0) 70%),
      linear-gradient(160deg, var(--paper-mid) 0%, var(--paper-light) 45%, var(--paper-mid) 75%, var(--paper-deep) 100%);
    font-family: "Oswald", "Arial Narrow", sans-serif;
    color: var(--ink);
  }
  .torn-corner {
    position: absolute;
    left: 0;
    top: 0;
    width: 300px;
    height: 280px;
  }
  .venue {
    position: absolute;
    left: 32px;
    top: 58px;
    display: flex;
    align-items: center;
    gap: 10px;
  }
  .venue-dot {
    flex: none;
    width: 16px;
    height: 16px;
    border-radius: 50%;
    background: var(--ink);
  }
  .venue-name {
    font-weight: 500;
    font-size: 26px;
    line-height: 1.05;
    letter-spacing: 1px;
    text-transform: uppercase;
  }
  .venue-name span { display: block; }
  .venue-city {
    position: absolute;
    left: 58px;
    top: 130px;
    font-weight: 500;
    font-size: 11px;
    letter-spacing: 9px;
    text-transform: uppercase;
  }
  .headline {
    position: absolute;
    right: 20px;
    top: 28px;
    text-align: right;
    text-transform: uppercase;
    line-height: 1;
  }
  .headline span { display: block; }
  .headline .line-light { font-weight: 300; font-size: 86px; letter-spacing: -2px; }
  .headline .line-medium { font-weight: 500; font-size: 120px; letter-spacing: -2px; margin-top: -4px; }
  .headline .line-bold { font-weight: 700; font-size: 168px; letter-spacing: -3px; margin-top: -8px; }
  .boombox {
    position: absolute;
    left: 34px;
    top: 528px;
    width: 352px;
    height: 300px;
    border-radius: 6px;
    background: linear-gradient(135deg, var(--box-tone-a) 0%, var(--box-tone-b) 100%);
  }
  .schedule {
    position: absolute;
    right: 24px;
    top: 606px;
    text-align: right;
    text-transform: uppercase;
    line-height: 1;
  }
  .schedule .regular {
    display: block;
    font-weight: 400;
    font-size: 44px;
    letter-spacing: -1px;
  }
  .schedule .day {
    display: block;
    font-weight: 700;
    font-size: 52px;
    letter-spacing: -1px;
  }
  .schedule .web {
    display: block;
    font-weight: 400;
    font-size: 18px;
    text-transform: none;
    margin-top: 2px;
  }
</style>
</head>
<body>
<div class="canvas">
  <div class="flyer">
    <svg class="torn-corner" viewBox="0 0 300 280" aria-hidden="true">
      <path d="M0 0 H290 L278 22 L262 40 L250 70 L232 92 L226 122 L204 150 L190 176 L168 196 L150 214 L120 232 L86 246 L54 252 L28 264 L0 272 Z" fill="var(--torn-grey)" stroke="var(--torn-edge)" stroke-width="2"/>
    </svg>

    <div class="venue">
      <span class="venue-dot"></span>
      <span class="venue-name"><span>Ridgeway</span><span>Hall</span></span>
    </div>
    <div class="venue-city">Lakeside</div>

    <h1 class="headline">
      <span class="line-light">Midnight</span>
      <span class="line-medium">Velvet</span>
      <span class="line-bold">Parade</span>
    </h1>

    <div class="boombox" role="img" aria-label="Worn silver and gold 1980s boombox cassette player"></div>

    <p class="schedule">
      <span class="regular">Every</span>
      <span class="regular">Week</span>
      <span class="regular">On a</span>
      <span class="day">Tuesday</span>
      <span class="web">www.ridgewayhall-nights.com</span>
    </p>
  </div>
</div>
</body>
</html>
```